New Managed IT company needs a business card

We are an IT management and support company that needs a business card design. I have a logo that I'll provide. Blues and blacks match the logo, but i'm open to anything. I want the card to help people take us seriously, but still have some energy and fun in it. The card should communicate stability and a solid company.

Target Market(s)

Target market includes Owners and Presidents at small businesses of 20 - 100 employees in the Pittsburgh PA area.

Industry/Entity Type

Information Technology

Contact Information for Business Card

i am open to other designs, but i imagine having only the logo on one side and then the logo plus all contact details on the other side.

Requirements
Must have
• Our logo
• Company name is optional if the logo makes it obvious
• A name - Cole Perrin
• A title - President
• A phone number - 724-XXX-XXXX
• A mobile phone number - 724-615-2748
• An email address - cperrin@techvaultgrid.com
• a website - techvaultgrid.com or www.techvaultgrid.com
Nice to have
• some people tell me the logo feels like a superhero theme, some fun with that idea might be good. I'm open to ideas.
Should not have
• stock photos of people or computers - especially old looking stuff.

```html
<!DOCTYPE html>
<html lang="en">
<head>
<meta charset="utf-8">
<title>Tech Vault Grid – Business Card</title>
<link href="https://fonts.googleapis.com/css2?family=Saira:wght@400;500;600&display=swap" rel="stylesheet">
<style>
  :root {
    --page: #2a2a2c;
    --card-front-top: #2c2e33;
    --card-front-bottom: #1c1d21;
    --card-back: #16171c;
    --brand-blue: #1f8fd6;
    --mark-grey: #a7a9ad;
    --text-white: #f1f2f4;
    --disc-outer: #c9ccd1;
    --disc-inner: #2a2c31;
  }
  * { margin: 0; padding: 0; box-sizing: border-box; }
  html, body {
    width: 1200px; height: 900px; overflow: hidden;
    background: var(--page);
    font-family: "Saira", "Helvetica Neue", Arial, sans-serif;
  }
  .stage { position: relative; width: 1200px; height: 900px; }
  .card {
    position: absolute; top: 301px;
    width: 514px; height: 296px;
    box-shadow: 0 6px 18px rgba(0,0,0,.45);
    overflow: hidden;
  }
  .card--front {
    left: 72px;
    background: radial-gradient(ellipse at 50% 55%, var(--card-front-top) 0%, var(--card-front-bottom) 85%);
  }
  .card--back { left: 615px; background: var(--card-back); }

  .brand-lockup {
    position: absolute; left: 0; right: 0; top: 0; bottom: 0;
    display: flex; align-items: center; justify-content: center; gap: 18px;
  }
  .brand-dot {
    width: 74px; height: 74px; border-radius: 50%;
    background: var(--mark-grey);
  }
  .brand-name {
    color: var(--mark-grey); font-weight: 500;
    font-size: 25px; letter-spacing: 4px; text-transform: uppercase;
  }

  .back-wordmark {
    position: absolute; left: 48px; top: 38px;
    color: var(--mark-grey); font-weight: 500;
    font-size: 20px; letter-spacing: 3px; text-transform: uppercase;
  }
  .person { position: absolute; left: 48px; top: 106px; line-height: 19px; font-size: 16px; }
  .person__name { color: var(--brand-blue); text-transform: uppercase; }
  .person__title { color: var(--text-white); text-transform: uppercase; }

  .contact { position: absolute; left: 48px; top: 160px; color: var(--text-white); font-size: 14px; line-height: 16px; list-style: none; }
  .contact li { display: flex; align-items: flex-start; gap: 6px; }
  .contact .gap { margin-top: 7px; }
  .contact svg { width: 11px; height: 11px; margin-top: 3px; flex: none; fill: var(--brand-blue); }
  .contact .upper { text-transform: uppercase; }

  .back-disc {
    position: absolute; right: 35px; top: 72px;
    width: 150px; height: 150px; border-radius: 50%;
    background: radial-gradient(circle at 50% 40%, var(--disc-inner) 55%, #1d1e22 100%);
    border: 6px solid var(--disc-outer);
  }
</style>
</head>
<body>
<main class="stage">
  <section class="card card--front" aria-label="Card front">
    <div class="brand-lockup">
      <span class="brand-dot"></span>
      <span class="brand-name">Tech Vault Grid</span>
    </div>
  </section>

  <section class="card card--back" aria-label="Card back">
    <div class="back-wordmark">Tech Vault Grid</div>
    <div class="person">
      <div class="person__name">Cole Perrin</div>
      <div class="person__title">President</div>
    </div>
    <ul class="contact">
      <li><svg viewBox="0 0 12 12"><path d="M2.5 1l2 2.2-1 1.3a6.5 6.5 0 0 0 4 4l1.3-1L11 9.5 9.6 11C5 10.5 1.5 7 1 2.4z"/></svg>724 390 5182</li>
      <li><svg viewBox="0 0 12 12"><path d="M3.5 0h5a1 1 0 0 1 1 1v10a1 1 0 0 1-1 1h-5a1 1 0 0 1-1-1V1a1 1 0 0 1 1-1zm.5 1.5v8h4v-8zM6 10.2a.6.6 0 1 0 0 1.2.6.6 0 0 0 0-1.2z"/></svg>724 615 2748</li>
      <li class="gap"><svg viewBox="0 0 12 12"><path d="M0 2.5h12v7H0zM0.8 3l5.2 3.6L11.2 3z"/></svg><span class="upper">cperrin@techvaultgrid.com</span></li>
      <li><svg viewBox="0 0 12 12"><path d="M6 0a6 6 0 1 0 0 12A6 6 0 0 0 6 0zm0 1.2c.6.6 1.2 2 1.3 4.2H4.7C4.8 3.2 5.4 1.8 6 1.2zM1.2 6.6h2.3c.1 1.6.4 3 .9 3.9A4.9 4.9 0 0 1 1.2 6.6zm0-1.2a4.9 4.9 0 0 1 3.2-3.9c-.5.9-.8 2.3-.9 3.9zm3.5 1.2h2.6C7.2 8.8 6.6 10.2 6 10.8c-.6-.6-1.2-2-1.3-4.2zm3.8 0h2.3a4.9 4.9 0 0 1-3.2 3.9c.5-.9.8-2.3.9-3.9zm0-1.2c-.1-1.6-.4-3-.9-3.9a4.9 4.9 0 0 1 3.2 3.9z"/></svg><span class="upper">www.techvaultgrid.com</span></li>
      <li class="gap"><svg viewBox="0 0 12 12"><path d="M6 0a4 4 0 0 1 4 4c0 3-4 8-4 8S2 7 2 4a4 4 0 0 1 4-4zm0 2.4a1.6 1.6 0 1 0 0 3.2 1.6 1.6 0 0 0 0-3.2z"/></svg><span>1450 Harmon Ridge Rd, Suite 200<br>Ellwood Falls, PA 16117</span></li>
    </ul>
    <div class="back-disc"></div>
  </section>
</main>
</body>
</html>
```